New River III Precinct 6x11 GOTV postcard

We require BOTH persuasive copy and high-impact layout for an oversized 6x11 political mailer. This might be one person, but it likely requires a specialized "creative team." of an experienced political strategist copywriter PLUS a graphic designer - so the words fit the exact layout block, and the visuals reinforce the psychological punch of the headline.

The goal is to remove all excuses a targeted audience of ~900 registered Democratic + ~1800 Unaffiliated voters in our precinct - have for not voting.

I need to be able to work by phone / online chat to iterate designs
I need to own the design in the top couple of software outputs that any printer service will require.

I want to experiment with very subtle background images as follows:
- Front of postcard that conveys "CHANGE" of not just seasons - but of encouraging change of precinct voter representation - so anything about fall foliage / conveyance of change tie-in is worthy of considering
- Back of postcard - any Appalachian long rage mountain view that includes 5-7 layers of hills in the distance.
Some photos as samples to consider.

Target Market(s)

~2,700 registered Democrats and Unaffiliated voters

Requirements
Must have
• We require BOTH persuasive copy and high-impact layout for an oversized 6x11 political mailer. This might be one person, but it likely requires a specialized "creative team." of an experienced political strategist copywriter PLUS a graphic designer - so the words fit the exact layout block, and the visuals reinforce the psychological punch of the headline
Nice to have
• subtle background photos

```html
<!DOCTYPE html>
<html lang="en">
<head>
<meta charset="utf-8">
<title>New River III Precinct Postcard</title>
<link href="https://fonts.googleapis.com/css2?family=Oswald:wght@400;500;600&family=Montserrat:wght@400;500;600;700&display=swap" rel="stylesheet">
<style>
:root{
  --page:#666666;
  --paper:#ffffff;
  --navy:#2a2d6e;
  --deep:#1c1a62;
  --ink:#2b2b2b;
  --check:#2f6fdc;
  --mist:#dbe6f3;
  --ridge:#2a649c;
}
*{box-sizing:border-box;margin:0;padding:0}
html,body{width:1041px;height:1200px;overflow:hidden;background:var(--page)}
body{position:relative;font-family:'Montserrat',sans-serif;color:var(--ink)}
.card{position:absolute;left:60px;width:920px;height:506px;background:var(--paper);overflow:hidden}
.card--front{top:56px}
.card--back{top:620px;height:507px}

/* front */
.mountain-view{position:absolute;left:0;right:0;top:200px;bottom:0;
  background:linear-gradient(180deg,rgba(255,255,255,0) 0%,var(--mist) 25%,#9fbde0 55%,#4f86bd 80%,var(--ridge) 100%)}
.greeting{position:absolute;left:12px;top:6px;font-family:'Oswald',sans-serif;font-weight:600;font-size:41px;line-height:1.1;color:var(--navy);letter-spacing:-.3px}
.letter{position:absolute;left:15px;top:53px;width:640px;font-size:9.6px;line-height:17.7px;color:var(--ink)}
.letter p+p{margin-top:17.7px}
.postal-box{position:absolute;left:843px;width:63px;height:66px;border:1px solid #555;background:#fff;display:flex;align-items:center;justify-content:center;text-align:center;font-size:6.5px;line-height:10.7px;font-weight:500;color:#222}
.postal-box--indicia{top:13px}
.postal-box--address{top:88px}
.voter-info{position:absolute;left:0;top:228px;width:430px;height:130px;background:var(--deep);border-radius:0 12px 12px 0;padding:15px 12px 0 13px;color:#fff;font-size:10.6px;font-weight:600;line-height:19.8px;text-transform:uppercase}

/* back */
.foliage{position:absolute;left:0;right:0;top:0;height:150px;
  background:linear-gradient(180deg,rgba(242,154,37,.55) 0%,rgba(210,66,27,.25) 40%,rgba(255,255,255,0) 100%)}
.headline{position:absolute;left:0;right:0;top:76px;text-align:center;font-family:'Oswald',sans-serif;font-weight:500;font-size:47px;line-height:1;color:var(--navy);padding-left:14px}
.headline-rule{position:absolute;left:342px;top:133px;width:237px;height:2px;background:var(--navy)}
.issue{position:absolute;left:15px;width:570px;padding-left:30px;font-size:9.3px;line-height:15.7px}
.issue-icon{position:absolute;left:0;top:-2px;width:25px;height:25px;border-radius:50%;background:var(--navy);display:flex;align-items:center;justify-content:center}
.issue-icon svg{width:14px;height:14px}
.issue-title{font-family:'Oswald',sans-serif;font-size:12.3px;font-weight:400;color:var(--navy);text-transform:uppercase}
.issue strong{font-weight:700}

.ballot{position:absolute;left:627px;top:155px;width:279px;height:337px;border:1px solid var(--navy);border-radius:11px;overflow:hidden;background:#fff}
.ballot-head{position:absolute;left:0;right:0;background:var(--navy);color:#fff;font-family:'Oswald',sans-serif;font-size:14.5px;line-height:17px;text-align:center;display:flex;align-items:center;justify-content:center}
.ballot-head--top{top:0;height:33px}
.ballot-head--mid{top:94px;height:43px}
.pick{position:absolute;left:0;right:0;text-align:center;font-size:10px;font-weight:500;line-height:15px;color:#111}
.tick{display:inline-block;width:10px;height:10px;vertical-align:-1px;margin-right:3px}
</style>
</head>
<body>

<section class="card card--front">
  <div class="mountain-view" role="img" aria-label="Misty layered Appalachian mountain ridges fading into the distance"></div>
  <h1 class="greeting">DEAR NEW RIVER III NEIGHBOR.</h1>
  <div class="letter">
    <p>We Live In A Representative Democracy. We Expect Our Representatives Will Exercise Independent Thinking And Support Policies And Legislation That Don't Harm Us - And That Reflect The Majority Views Of Precinct Citizens. But Our Current Representatives Have Stopped Listening - They Are Now Bringing Harmful Policies Straight To Watauga County. It's Time To Hold Them Accountable And Vote Them Out. Make No Mistake: In 2026, Every Election Is Partisan. Even Judicial Seats Are Now Tied Directly To State Platforms.</p>
    <p>Any Candidate WHO Refuses To Publicly Condemn Raleigh's Gerrymandered Overreach Into Watauga Politics-or Refuses To Fight Funding Cuts For Our Healthcare, Education, And Environmental Justice - Is Actively Supporting.These Harmful Policies. They Are Hoping Their Silence Fools You. Don't Be Fooled. This November, Vote For Change.</p>
  </div>
  <div class="postal-box postal-box--indicia">PRSRT STD<br>ECRWSS<br>U.S. Postage<br>PAID EDDM<br>Retail</div>
  <div class="postal-box postal-box--address">LOCAL<br>POSTAL<br>CUSTOMER</div>
  <div class="voter-info">You are a registered voter in Watauga County, you reside in precinct: New River III poui ng places available to you are: location,. 2, 3 early voting starts on: deadline to apply for mail-in ballots know the rules to ensure your mail-in-ballot counts</div>
</section>

<section class="card card--back">
  <div class="foliage" role="img" aria-label="Scattered autumn leaves in red, orange and yellow along the top edge"></div>
  <h2 class="headline">VOTE FOR NEW REPRESENTATION</h2>
  <div class="headline-rule"></div>

  <div class="issue" style="top:152px">
    <span class="issue-icon"><svg viewBox="0 0 14 14"><circle cx="7" cy="6" r="4" fill="none" stroke="#fff" stroke-width="1.4"/><path d="M3 12h8" stroke="#fff" stroke-width="1.4"/></svg></span>
    <span class="issue-title">Local Pain-Thanks To Current Representatives</span> - And sadly, to avoid accountability, they've cleverly delayed many /most impacts until AFTER the 2026 election. <strong>VOTE FOR CHANGE</strong>
  </div>
  <div class="issue" style="top:199px">
    <span class="issue-icon"><svg viewBox="0 0 14 14"><circle cx="7" cy="7" r="5" fill="none" stroke="#fff" stroke-width="1.4"/><path d="M7 4v6M5.5 5.5h3M5.5 8.5h3" stroke="#fff" stroke-width="1.1"/></svg></span>
    <span class="issue-title">Family Budget</span> - Exploded costs for everything: groceries, gas, car insurance, rent.
  </div>
  <div class="issue" style="top:228px">
    <span class="issue-icon"><svg viewBox="0 0 14 14"><path d="M7 12L2 7a2.8 2.8 0 0 1 5-3 2.8 2.8 0 0 1 5 3z" fill="#fff"/></svg></span>
    <span class="issue-title">Health</span> - Expired subsidies, tax credits mean Im in NC will lose coverage or pay more. 50% cuts to Hospitals, Mental Health facilities; rural facilities will be closing
  </div>
  <div class="issue" style="top:272px">
    <span class="issue-icon"><svg viewBox="0 0 14 14"><circle cx="7" cy="7" r="5" fill="none" stroke="#fff" stroke-width="1.4"/><path d="M4 10l6-6" stroke="#fff" stroke-width="1.4"/></svg></span>
    <span class="issue-title">Reproductive Rights</span> - Government authoritarian intrusion - censure women's rights.
  </div>
  <div class="issue" style="top:299px">
    <span class="issue-icon"><svg viewBox="0 0 14 14"><path d="M2 4l5-2 5 2v7l-5-2-5 2z" fill="none" stroke="#fff" stroke-width="1.3"/></svg></span>
    <span class="issue-title">Education</span> - Watauga $2.2mm shortfall personnel cuts, freezes in hiring, teacher training. Abandoning civil rights of Special Ed students to HHS and DOL
  </div>
  <div class="issue" style="top:336px">
    <span class="issue-icon"><svg viewBox="0 0 14 14"><path d="M1.5 7.5L7 2.5l5.5 5H11v4.5H8.5V9h-3v3H3V7.5z" fill="#fff"/></svg></span>
    <span class="issue-title">Housing</span> - 25% of renters are spending over 50% of income on rent. Especially bad locally; predatory leasing terms and skyrocketing rents. Proposed legislation is transforming HUDwith the goal of getting rid of Section 8 housing that cares for vulnerable populations.
  </div>
  <div class="issue" style="top:390px">
    <span class="issue-icon"><svg viewBox="0 0 14 14"><circle cx="7" cy="7" r="5" fill="none" stroke="#fff" stroke-width="1.3"/><path d="M8 3.5L5.5 7.5h3L6 10.5" fill="none" stroke="#fff" stroke-width="1.2"/></svg></span>
    <span class="issue-title">Energy</span> - In 2022 Boone achieved 100% renewable energy in town buildings; this is now being destroyed by repeal of renewable energy project funding: Highland State Innovation District prepares renewable workforce technologies-all this is now in limbo.
  </div>
  <div class="issue" style="top:443px">
    <span class="issue-icon"><svg viewBox="0 0 14 14"><circle cx="7" cy="7" r="5" fill="none" stroke="#fff" stroke-width="1.3"/><path d="M3 6c2 0 2 2 4 2s1 3 3 3M6 2.5c0 2 2 2 3 1" fill="none" stroke="#fff" stroke-width="1.1"/></svg></span>
    <span class="issue-title">Environment</span> - Reduced protections from coal ash pond leaks threaten public health. Corporations not held responsible for damage; public picks up the tab. Environmental Justice enforcement no longera priority. Logging in Watauga with no public oversight. It's the "haz-mat" model do nothing, wait for catastrophe, then fix it.
  </div>

  <aside class="ballot">
    <div class="ballot-head ballot-head--top">SAMPLE BALLOT RECOMMENDATIONS</div>
    <div class="pick" style="top:44px"><svg class="tick" viewBox="0 0 10 10"><circle cx="5" cy="5" r="5" fill="#2f6fdc"/><path d="M2.8 5.2l1.5 1.5 3-3" fill="none" stroke="#fff" stroke-width="1.3"/></svg>US Senate - RAY CALLOWAY</div>
    <div class="pick" style="top:66px"><svg class="tick" viewBox="0 0 10 10"><circle cx="5" cy="5" r="5" fill="#2f6fdc"/><path d="M2.8 5.2l1.5 1.5 3-3" fill="none" stroke="#fff" stroke-width="1.3"/></svg>US House-district 5 - CHET HOLLISTER</div>
    <div class="ballot-head ballot-head--mid">REQMT TO SHOW ID FOR VOTERS<br>NOT IN PERSON-NO</div>
    <div class="pick" style="top:150px"><svg class="tick" viewBox="0 0 10 10"><circle cx="5" cy="5" r="5" fill="#2f6fdc"/><path d="M2.8 5.2l1.5 1.5 3-3" fill="none" stroke="#fff" stroke-width="1.3"/></svg>State Senate District 47 - FRANK DELMORE</div>
    <div class="pick" style="top:180px"><svg class="tick" viewBox="0 0 10 10"><circle cx="5" cy="5" r="5" fill="#2f6fdc"/><path d="M2.8 5.2l1.5 1.5 3-3" fill="none" stroke="#fff" stroke-width="1.3"/></svg>House Of Rep's District 93 - CARLA WHITTEN</div>
    <div class="pick" style="top:211px"><svg class="tick" viewBox="0 0 10 10"><circle cx="5" cy="5" r="5" fill="#2f6fdc"/><path d="M2.8 5.2l1.5 1.5 3-3" fill="none" stroke="#fff" stroke-width="1.3"/></svg>NC Supreme Court - ALMA EVERETT</div>
    <div class="pick" style="top:242px"><svg class="tick" viewBox="0 0 10 10"><circle cx="5" cy="5" r="5" fill="#2f6fdc"/><path d="M2.8 5.2l1.5 1.5 3-3" fill="none" stroke="#fff" stroke-width="1.3"/></svg>NC Court Of Appeals-seat 1 - JOEL ASHFORD</div>
    <div class="pick" style="top:272px"><svg class="tick" viewBox="0 0 10 10"><circle cx="5" cy="5" r="5" fill="#2f6fdc"/><path d="M2.8 5.2l1.5 1.5 3-3" fill="none" stroke="#fff" stroke-width="1.3"/></svg>NC Court Of Appeals-seat 2 - TOBIN HARWELL</div>
    <div class="pick" style="top:296px"><svg class="tick" viewBox="0 0 10 10"><circle cx="5" cy="5" r="5" fill="#2f6fdc"/><path d="M2.8 5.2l1.5 1.5 3-3" fill="none" stroke="#fff" stroke-width="1.3"/></svg>NC Court Of Appeals-seat 3<br>CORINNE WALSH</div>
  </aside>
</section>

</body>
</html>
```